Banner ad *

Replace blue banner

- An Overview / Background of the Business & Services
- We are online Wine/Spirits Merchant we ship wine throughout the USA
excluding certain states
- The Target Market / Audience you are trying to reach
- Consumers looking for online sources for hard to find wines and
vintages, our listings have detailed reviews from wine publications as long
as winery descriptions and images
- Design Specifics; any preferences or ideas for Style, Colour, Imagery,
etc
- Whichever colors will work best with wine or spirits consumers, we
have blue in our sign locally but burgundy is a rich color that is often
used with wine.

Target Market(s)

Wine drinkers ages 35-60

Industry/Entity Type

Business

Font styles to use
Serif

Colors
886aae
3176b5

Requirements
Must have
• Wine
Nice to have
• Whiskey
Should not have
• Underage people in images

```html
<!DOCTYPE html>
<html lang="en">
<head>
<meta charset="utf-8">
<title>Caskwell Inc. — Banner</title>
<link rel="stylesheet" href="https://fonts.googleapis.com/css2?family=Roboto+Condensed:ital,wght@1,300;1,700&display=swap">
<style>
  :root {
    --ink-white: #ffffff;
    --cellar-black: #0a0710;
    --cellar-navy: #141a3a;
    --cellar-blue: #2b3f8f;
    --cellar-burgundy: #5a0b1c;
    --cellar-red: #8e1325;
    --page-bg: #000000;
  }
  html, body {
    margin: 0;
    padding: 0;
    width: 1200px;
    height: 410px;
    overflow: hidden;
    background: var(--page-bg);
  }
  .banner {
    position: relative;
    width: 1200px;
    height: 410px;
    overflow: hidden;
    font-family: "Roboto Condensed", "Arial Narrow", sans-serif;
    color: var(--ink-white);
  }
  .banner__cellar-photo {
    position: absolute;
    inset: 0;
    background:
      radial-gradient(ellipse 260px 200px at 190px 260px, rgba(160, 30, 45, 0.85), transparent 70%),
      radial-gradient(ellipse 220px 260px at 60px 120px, rgba(55, 70, 160, 0.55), transparent 75%),
      radial-gradient(ellipse 520px 260px at 820px 170px, rgba(142, 19, 37, 0.75), transparent 75%),
      radial-gradient(ellipse 300px 200px at 1180px 380px, rgba(43, 63, 143, 0.7), transparent 75%),
      linear-gradient(100deg, var(--cellar-navy) 0%, var(--cellar-black) 35%, var(--cellar-burgundy) 65%, var(--cellar-black) 100%);
  }
  .banner__headline {
    position: absolute;
    left: 0;
    right: 0;
    top: 124px;
    margin: 0;
    text-align: center;
    font-weight: 700;
    font-style: italic;
    font-size: 82px;
    line-height: 1;
    letter-spacing: 0.5px;
    padding-left: 4px;
  }
  .banner__tagline {
    position: absolute;
    left: 0;
    right: 0;
    top: 204px;
    margin: 0;
    text-align: center;
    font-weight: 300;
    font-style: italic;
    font-size: 53px;
    line-height: 1;
  }
</style>
</head>
<body>
  <section class="banner">
    <div class="banner__cellar-photo" role="img" aria-label="Wine bottle necks in the foreground before a dimly lit wine cellar with wooden racks in red and blue light"></div>
    <h1 class="banner__headline">CASKWELL INC.</h1>
    <p class="banner__tagline">Specialists in hard to find wines and vintages</p>
  </section>
</body>
</html>
```